A5 Patient Information Booklet (Chiropractic Clinic) 4-8 pages

Here’s a polished, professional rewrite of your full brief and content, with clearer structure, corrected language, and a premium tone:

---

**Project Title:** Premium Patient Information Brochure (Chiropractic & Wellness Clinic)

---

### **Overview**

We are a health and wellness clinic seeking a premium, high-end patient information brochure to provide following a patient’s initial consultation and first treatment.

The purpose of this booklet is to:

* Reinforce trust and professionalism
* Help patients understand what to expect next
* Encourage adherence to care recommendations
* Position the clinic as calm, expert-led, and results-driven

---

### **Format**

* 4–8 page booklet (A5 or similar size)
* Print-ready and digital versions required

---

### **Target Audience**

Patients who have just completed their initial consultation and may have begun treatment. They may already be experiencing physical or mental changes, so the brochure should guide, reassure, and educate them on what comes next.

---

### **Tone & Style**

* Premium, calm, and reassuring
* Modern wellness aesthetic (not overly clinical)
* Clean layout with minimal clutter
* Soft, neutral colour palette (whites, creams, muted greens, soft blues)
* Elegant typography (e.g. Montserrat / Lato)
* High-end, trustworthy, and professional feel

---

### **Key Messages**

#### 1. Listen to Your Body

Patients may feel different after treatment. Reassure them that this is normal and part of the healing process.

#### 2. Post-Treatment Advice

* Stay well hydrated
* Rest if needed
* Avoid overexertion if the body requires recovery

#### 3. Healing is a Journey (Core Concept)

A strong visual metaphor of a **“road to recovery”** or **journey** should be central to the design.

This journey should clearly illustrate three phases:

* **Phase 1: Initial Care (Weeks 1–6)**
Focus: Reducing pain/discomfort, calming the body, and initiating response to treatment

* **Phase 2: Corrective Care (Weeks 6–12)**
Focus: Addressing underlying issues, improving function, and creating lasting change

* **Phase 3: Wellness / Maintenance (Ongoing)**
Focus: Maintaining progress, preventing relapse, and supporting long-term wellbeing

**Important:**

* Emphasise that this is not a quick fix
* Progress requires time and consistency
* Each patient follows an individualised care plan
* The journey should feel structured, positive, and achievable

#### 4. Personalised Care

Reinforce that every treatment plan is tailored specifically to the individual.

#### 5. Professional Reassurance

Patients should feel confident they are in expert hands and supported throughout their journey.

---

### **Design Direction**

* Use imagery that reflects calmness, progression, and wellness (e.g. pathways, nature, soft gradients)
* Avoid generic stock imagery
* **Only use original clinic images from website and social media**
* Prioritise white space and clarity
* Aim for a luxury spa/medical hybrid aesthetic

---

## **Content Structure (Page-by-Page)**

### **Front Cover**

* Clean, minimal, premium design
* Clinic branding

---

### **Page 1: Patient Case Summary**

**Title:** *Welcome to Larkmoor Spine Studio*

Thank you for choosing Larkmoor Spine Studio.

This booklet is designed to guide you through:

* What we found during your initial consultation
* Your personalised recommended treatment plan
* Your road to recovery
* Long-term wellness care
* Why we take the approach we do

---

### **Page 2: Your Care Journey**

**Stage 1: Your Initial Consultation**

Today we completed a comprehensive assessment of your health and function, including:

* Full case history and discussion of your symptoms and goals
* Orthopaedic and neurological testing
* Postural and movement assessment
* Initial treatment (where appropriate)

**What this tells us:**

* How your body is currently functioning
* Where areas of stress or dysfunction may be present
* The most appropriate and effective path forward for your care

---

### **Page 3: Your Suggested Treatment Plan**

Based on today’s findings, your recommended care plan is:

**______ treatments over ______ weeks**

This should be viewed alongside your *Road to Recovery* to help you understand what to expect.

We have also discussed:

* Expected timelines for improvement
* Available payment options

**After Treatment:**
It is common to feel different following treatment. This is a normal response as your body begins to adapt and respond.

We recommend:

* Staying well hydrated
* Allowing time for rest and recovery
* Avoiding overexertion if your body feels it needs it

---

### **Page 4: What to Expect Next**

Healing is not always linear—it is a process that occurs over time.

Your care will typically progress through the following stages:

* **Relief Care**
Focused on reducing discomfort and calming the body

* **Corrective Care**
Focused on addressing underlying issues and improving function
(This phase may include prescribed exercises)

* **Maintenance / Wellness Care**
Focused on sustaining progress, preventing recurrence, and supporting long-term health

---

### **Page 5: Understanding Chiropractic Care**

**What is Chiropractic?**
Chiropractic care focuses on the relationship between the spine, nervous system, and overall body function.

By improving spinal movement and alignment, chiropractic care helps support the nervous system, allowing the body to function and heal more effectively.

**About Larkmoor Spine Studio**
At Larkmoor Spine Studio, our approach is centred around personalised, patient-focused care. We aim to not only relieve symptoms but to address underlying causes and support long-term wellbeing.

---

### **Back Page**

* Clinic contact details
* Website
* Social media icons/handles

**Closing Message:**
“A healthier, stronger you—supported every step of the way.”

---

### **Deliverables**

* Print-ready PDF
* Editable source files

---

### **Additional Notes**

* The brochure should feel valuable and worth keeping
* Encourage long-term care in a subtle, non-pushy way
* Maintain clarity, readability, and strong visual hierarchy
* Balance professionalism with warmth and approachability

---

If you’d like, I can also turn this into **actual brochure copy (fully written, patient-facing text)** or help you refine it further for a designer.

Target Market(s)

Existing patients who want to feel better and look after themselves that is given after their initil consultation appointment

Industry/Entity Type

Chiropractic, wellness, health

Font styles to use
Other font styles liked:
• Montserrat or Lato

Colors
0094D4
00A9DD
6FCCEA
C7EBF8
E9F6FB
00AB8E
00BBA5
67D7C9
C6EFE9
E9F9F6
6B429C
8869AF
B7A5CE
E3DAEB
F3F0F8

Requirements
Must have
• my own photos, look premium wellness, be clear and simple to understand for patients journey or what to expect next and over time
Nice to have
• USe my social media/website for ideas
Should not have
• generic photos and images

```html
<!DOCTYPE html>
<html lang="en">
<head>
<meta charset="utf-8">
<title>Larkmoor Spine Studio – Patient Booklet Pages</title>
<link href="https://fonts.googleapis.com/css2?family=Montserrat:wght@600;700;800&family=Lato:wght@400;700&display=swap" rel="stylesheet">
<style>
:root{
  --stage:#201e21;
  --teal:#16a6a0;
  --teal-band:#1bafa7;
  --teal-dark:#0f7f86;
  --ink:#1f1f1f;
  --cyan-pale:#e5f8fc;
  --pink:#f48bbd;
  --purple:#9b86c2;
  --blue:#5e8ec8;
  --pink-box:#fdf0f7;
  --dot:#a48ad0;
  --white:#ffffff;
}
*{box-sizing:border-box;margin:0;padding:0}
html,body{width:877px;height:1200px;overflow:hidden}
body{background:var(--stage);position:relative;font-family:'Lato',sans-serif;color:var(--ink)}
.page{position:absolute;width:367px;height:521px;overflow:hidden;background:var(--white)}
.page--cover{left:58px;top:60px;background:var(--cyan-pale)}
.page--about{left:451px;top:60px}
.page--journey{left:57px;top:615px}
.page--care{left:452px;top:615px}
.abs{position:absolute}
.photo{position:absolute}
.h{font-family:'Montserrat',sans-serif;font-weight:700;position:absolute}
.body-text{position:absolute;font-size:8.4px;line-height:10.5px;text-align:justify}
.brand-name{font-family:'Montserrat',sans-serif;font-weight:700;color:var(--teal-dark);position:absolute;text-align:center;white-space:nowrap}
.brand-dot{position:absolute;border-radius:50%;border:2px solid var(--teal)}

/* cover */
.cover-art{position:absolute;left:0;top:0}
.cover-title{left:0;width:367px;text-align:center;color:var(--teal);font-size:21px;line-height:29px;top:306px;font-weight:800}
.form-row{position:absolute;left:56px;width:256px;font-size:11px;display:flex;align-items:flex-end}
.form-row span{width:72px}
.form-row i{flex:1;border-bottom:0.8px solid #444;height:1px;margin-bottom:2px}

/* journey page */
.journey-head{position:absolute;left:0;top:0;width:367px;height:135px;background:linear-gradient(90deg,#f78ab9 0%,#b68fc1 50%,#6d8cc6 100%)}
.journey-title{left:13px;top:13px;color:var(--white);font-size:18.4px;white-space:nowrap}
.phase-photo{top:49px;width:109px;height:57px;border-radius:5px}
.phase-label{top:111px;color:var(--white);font-size:10.8px}
.sub-h{font-size:11.6px;color:var(--ink)}
.para{position:absolute;font-size:9.2px;line-height:12.5px}
.pink-box{position:absolute;background:var(--pink-box);border-radius:4px}
.bullets{list-style:none;font-size:9.2px;line-height:15.8px}
.bullets li{position:relative;padding-left:13px}
.bullets li::before{content:"";position:absolute;left:0;top:5px;width:5px;height:5px;border-radius:50%;background:var(--dot)}
.footer{position:absolute;left:0;top:481px;width:367px;height:40px;background:var(--teal-band);color:var(--white)}
.call-label{left:45px;top:7px;font-size:7.6px;font-family:'Montserrat',sans-serif;font-weight:700}
.call-number{left:43px;top:16px;font-size:13.4px}
.foot-address{right:9px;top:9px;font-size:7.6px;font-family:'Montserrat',sans-serif;font-weight:700}
.foot-web{right:9px;top:20px;font-size:10px}

/* care page */
.care-head-panel{position:absolute;left:0;top:0}
.care-title{left:136px;top:9px;font-size:19.5px;color:var(--ink)}
.care-intro{left:136px;top:36px;font-size:9.8px;line-height:14px;width:200px}
.expect-title{left:15px;top:195px;font-size:12.6px}
.tip-icon{position:absolute;width:30px;height:30px}
.tip-title{font-size:10.8px;color:var(--ink)}
.tip-text{position:absolute;font-size:8.8px;line-height:10.2px}
.help-band{position:absolute;left:0;top:361px;width:367px;height:160px;background:var(--teal-band);color:var(--white)}
.help-title{left:19px;top:12px;font-size:13px;color:var(--white)}
.help-intro{left:20px;top:31px;font-size:9.4px;line-height:12px;width:200px}
.help-list{position:absolute;left:22px;top:63px;list-style:none;font-size:9.4px;line-height:16.6px;font-family:'Montserrat',sans-serif;font-weight:600}
.help-list li{position:relative;padding-left:16px}
.help-list li::before{content:"";position:absolute;left:0;top:5px;width:6px;height:6px;border-radius:50%;background:var(--white)}
</style>
</head>
<body>

<!-- Cover -->
<section class="page page--cover">
  <svg class="cover-art" width="367" height="290" viewBox="0 0 367 290">
    <defs>
      <linearGradient id="coverPhoto" x1="0" y1="0" x2="1" y2="1">
        <stop offset="0" stop-color="#9a9a9a"/><stop offset="0.5" stop-color="#5d5d5d"/><stop offset="1" stop-color="#2e2e2e"/>
      </linearGradient>
      <linearGradient id="waveBand" x1="0" y1="0" x2="1" y2="0">
        <stop offset="0" stop-color="#f08abb"/><stop offset="0.5" stop-color="#a88ac6"/><stop offset="1" stop-color="#5a8cc6"/>
      </linearGradient>
    </defs>
    <path role="img" aria-label="Black and white photo of the chiropractor treating a patient's neck" fill="url(#coverPhoto)"
      d="M0,0 H367 V234 C320,236 275,225 240,205 C205,185 175,168 140,168 C95,168 40,190 0,230 Z"/>
    <path fill="url(#waveBand)"
      d="M0,230 C40,190 95,168 140,168 C175,168 205,185 240,205 C275,225 320,236 367,234 V250 C320,250 280,240 245,220 C210,198 180,182 142,180 C100,180 45,205 0,253 Z"/>
  </svg>
  <div class="brand-dot" style="left:162px;top:222px;width:44px;height:44px"></div>
  <div class="brand-name" style="left:0;width:367px;top:273px;font-size:10px">LARKMOOR SPINE STUDIO</div>
  <h1 class="h cover-title">Align your body,<br>elevate your wellbeing</h1>
  <div class="form-row" style="top:383px"><span>Patient Name</span><i></i></div>
  <div class="form-row" style="top:412px"><span>Date</span><i></i></div>
  <div class="form-row" style="top:440px"><span>Treatments</span><i></i></div>
  <div class="form-row" style="top:472px"><span>Weeks</span><i></i></div>
</section>

<!-- About -->
<section class="page page--about">
  <div class="photo" role="img" aria-label="Photo of the chiropractor adjusting a patient's neck on a treatment table by a bright window" style="left:199px;top:0;width:168px;height:168px;background:linear-gradient(160deg,#dcd8cf,#9a8b7e 60%,#6b6a80)"></div>
  <h2 class="h" style="left:13px;top:25px;font-size:12px">What is Chiropractic Care?</h2>
  <p class="body-text" style="left:13px;top:47px;width:163px">Chiropractic care focuses on how your body moves, functions, and heals as a whole. By improving the alignment and mobility of the spine and joints, it helps reduce pressure on the nervous system, allowing your body to function more efficiently. Rather than simply masking symptoms, this approach supports your body’s natural ability to adapt, recover, and maintain long-term health.</p>

  <div class="photo" role="img" aria-label="Photo of the chiropractor treating a patient lying on a table in the clinic" style="left:0;top:165px;width:169px;height:171px;background:linear-gradient(150deg,#e4e4de,#a3957f 55%,#7a5a48)"></div>
  <h2 class="h" style="left:189px;top:189px;font-size:12px">Your Chiropractor</h2>
  <p class="body-text" style="left:189px;top:209px;width:163px">At Larkmoor Spine Studio, your care is led by chiropractor Maren, who takes a personalised, hands-on approach to your health. Every consultation is focused on understanding your body, your lifestyle, and your goals—so your treatment plan is tailored specifically to you. Maren combines clinical expertise with a calm, supportive environment to help you feel confident, informed, and in control of your recovery journey.</p>

  <h2 class="h" style="left:13px;top:359px;font-size:12px">About Larkmoor Spine Studio</h2>
  <p class="body-text" style="left:13px;top:381px;width:165px">At Larkmoor Spine Studio, we believe that true health is built over time—not achieved through quick fixes. Our approach is centred around personalised care, attention to detail, and long-term results. We work with you to not only relieve symptoms, but to improve how your body functions and performs in everyday life. Every step of your journey is guided with care, clarity, and a focus on lasting wellbeing.</p>
  <div class="photo" role="img" aria-label="Photo of the chiropractor explaining the spine on an anatomical skeleton model" style="left:199px;top:348px;width:168px;height:173px;background:linear-gradient(150deg,#ece6df,#c9b7a6 50%,#8a6a55)"></div>
</section>

<!-- Care journey -->
<section class="page page--journey">
  <div class="journey-head"></div>
  <h2 class="h journey-title">Your Recommended Care Journey</h2>
  <div class="photo phase-photo" role="img" aria-label="Photo of hands treating a patient's shoulder" style="left:12px;background:linear-gradient(150deg,#eee9e4,#b39783)"></div>
  <div class="photo phase-photo" role="img" aria-label="Photo of the chiropractor with a skeleton model" style="left:128px;background:linear-gradient(150deg,#ebe4dc,#a98a72)"></div>
  <div class="photo phase-photo" role="img" aria-label="Photo of smiling patients together in the clinic" style="left:245px;background:linear-gradient(150deg,#c6d3d8,#8d6e58)"></div>
  <div class="h phase-label" style="left:13px">Relief Phase</div>
  <div class="h phase-label" style="left:128px">Correction Phase</div>
  <div class="h phase-label" style="left:245px">Wellness Phase</div>

  <div class="photo" role="img" aria-label="Photo of a patient doing a resistance band exercise" style="left:11px;top:149px;width:109px;height:138px;border-radius:5px;background:linear-gradient(160deg,#e8e8e6,#6fae8a 50%,#3b3b3b)"></div>
  <h3 class="h sub-h" style="left:132px;top:151px">Why Consistency Matters</h3>
  <p class="para" style="left:132px;top:170px;width:200px">Just like exercise or physiotherapy, improvement happens with consistent care.</p>
  <p class="para" style="left:132px;top:198px">Attending your scheduled appointments helps us:</p>
  <div class="pink-box" style="left:132px;top:230px;width:199px;height:57px">
    <ul class="bullets" style="margin:4px 0 0 10px">
      <li>Monitor your progress</li>
      <li>Adjust your treatment when needed</li>
      <li>Support long-term recovery</li>
    </ul>
  </div>

  <h3 class="h sub-h" style="left:13px;top:304px">How You Can Support Your Recovery</h3>
  <p class="para" style="left:13px;top:323px;width:220px">Your recovery is a partnership between you and your chiropractor.</p>
  <p class="para" style="left:13px;top:359px">Attending your scheduled appointments helps us:</p>
  <div class="pink-box" style="left:12px;top:381px;width:225px;height:88px">
    <ul class="bullets" style="margin:9px 0 0 9px">
      <li>Following your recommended care schedule</li>
      <li>Performing any home exercises provided</li>
      <li>Maintaining good posture habits</li>
      <li>Staying active where possible</li>
    </ul>
  </div>
  <div class="photo" role="img" aria-label="Photo of the chiropractor assessing a patient's back posture" style="left:250px;top:307px;width:107px;height:165px;border-radius:5px;background:linear-gradient(160deg,#eeeae6,#c9b9a8 40%,#3a4258)"></div>

  <div class="footer">
    <svg class="abs" style="left:12px;top:9px" width="22" height="22" viewBox="0 0 22 22">
      <rect width="22" height="22" rx="4" fill="#fff"/>
      <path d="M7.2 4.5c.6-.3 1.2 0 1.5.5l1.2 2.4c.3.5.1 1.1-.3 1.4l-1 .8c.7 1.6 2 2.9 3.6 3.6l.8-1c.3-.4.9-.6 1.4-.3l2.4 1.2c.5.3.8.9.5 1.5l-.6 1.4c-.3.6-.9 1-1.6.9C9.5 16.4 5.6 12.5 5.1 6.9c-.1-.7.3-1.3.9-1.6z" fill="var(--teal-band)"/>
    </svg>
    <div class="abs call-label">CALL US NOW</div>
    <div class="abs call-number">(555) 014 2290</div>
    <div class="abs foot-address">Chiropractic &amp; Wellness, 12 Orchard Lane, Larkmoor, LM4 7QT</div>
    <div class="abs foot-web">www.larkmoorspinestudio.com</div>
  </div>
</section>

<!-- Care here -->
<section class="page page--care">
  <svg class="care-head-panel" width="367" height="78" viewBox="0 0 367 78">
    <path d="M96,0 H367 V78 H118 C104,66 118,50 106,34 C96,22 92,10 96,0 Z" fill="#dff5f8"/>
  </svg>
  <div class="brand-dot" style="left:32px;top:10px;width:40px;height:40px"></div>
  <div class="brand-name" style="left:0;width:104px;top:57px;font-size:6.6px">LARKMOOR SPINE STUDIO</div>
  <h2 class="h care-title">Your Care Here</h2>
  <p class="abs care-intro">Thank you for visiting Larkmoor Spine Studio for your chiropractic consultation.</p>
  <div class="photo" role="img" aria-label="Photo of the chiropractor's hands working on a patient's back" style="left:0;top:78px;width:367px;height:108px;background:linear-gradient(100deg,#8a6a55,#d9cfc6 45%,#efebe7 75%,#cfc3b8)"></div>

  <h2 class="h expect-title">What to Expect After Your Treatment</h2>

  <svg class="tip-icon" style="left:11px;top:223px" viewBox="0 0 30 30"><circle cx="15" cy="15" r="15" fill="var(--teal)"/><path d="M15 7c3 4 5 6.5 5 9a5 5 0 0 1-10 0c0-2.5 2-5 5-9z" fill="#fff"/></svg>
  <h3 class="h tip-title" style="left:49px;top:223px">Stay Hydrated</h3>
  <p class="tip-text" style="left:49px;top:238px;width:115px">Drinking plenty of water supports your body’s natural recovery process.</p>

  <svg class="tip-icon" style="left:171px;top:223px" viewBox="0 0 30 30"><circle cx="15" cy="15" r="15" fill="var(--teal)"/><path d="M11 10l-3 3 3 3M8 13h9a4 4 0 0 1 0 8h-6" fill="none" stroke="#fff" stroke-width="2" stroke-linecap="round" stroke-linejoin="round"/></svg>
  <h3 class="h tip-title" style="left:208px;top:223px">Rest When Needed</h3>
  <p class="tip-text" style="left:208px;top:238px;width:125px">Give your body time to recover. Avoid overexertion if your body feels like it needs rest.</p>

  <svg class="tip-icon" style="left:11px;top:283px" viewBox="0 0 30 30"><circle cx="15" cy="15" r="15" fill="var(--teal)"/><path d="M15 6l7 3v5c0 5-3 8-7 10-4-2-7-5-7-10V9z" fill="none" stroke="#fff" stroke-width="1.8"/><path d="M11.5 15l2.5 2.5 4.5-5" fill="none" stroke="#fff" stroke-width="1.8" stroke-linecap="round"/></svg>
  <h3 class="h tip-title" style="left:49px;top:283px">Trust the Process</h3>
  <p class="tip-text" style="left:49px;top:298px;width:122px">Meaningful, lasting change takes time. Each step of your care plan is designed to support long-term results—not just short-term relief.</p>

  <svg class="tip-icon" style="left:171px;top:283px" viewBox="0 0 30 30"><circle cx="15" cy="15" r="15" fill="var(--teal)"/><path d="M6 15h5l2-5 4 10 2-5h5" fill="none" stroke="#fff" stroke-width="1.8" stroke-linecap="round" stroke-linejoin="round"/></svg>
  <h3 class="h tip-title" style="left:208px;top:283px">Listen to Your Body</h3>
  <p class="tip-text" style="left:208px;top:298px;width:120px">You may feel relief, mild soreness, or changes in how your body moves—these are all normal signs of adjustment.</p>

  <div class="help-band">
    <h2 class="h help-title">Why Chiropractic Care Helps</h2>
    <p class="abs help-intro">Your spine protects your nervous system, which controls every function in your body.</p>
    <ul class="help-list">
      <li>Pain and stiffness</li>
      <li>Reduced mobility</li>
      <li>Muscle tension</li>
      <li>Headaches or nerve irritation</li>
      <li>Poor posture and fatigue</li>
    </ul>
    <div class="photo" role="img" aria-label="Photo of the chiropractor treating a patient's leg" style="left:228px;top:13px;width:129px;height:138px;border-radius:5px;background:linear-gradient(160deg,#eee9e5,#7f98b5 45%,#6a5446)"></div>
  </div>
</section>

</body>
</html>
```